Recruiting Firm Need Professional, Modern Tri-Fold Brochure for their United States Based Business

-We need a professional, modern TRI-FOLD brochure design that can help generate business for our recruiting firm. We need an impressive brochure.
- Please use the about us website content and attached website content. Website: www.pelvorstaffingpartners.example
- Please use logo files attached.
- Please note: This brochure will be the starting point for an upgraded website design so we are NOT looking for a brochure to look like our current website.
- We want potential clients to want to do business with us just based on the brochure look and feel alone.

Target Market(s)

small, medium, and large companies who need administrative, human resources, and accounting talent

Industry/Entity Type

Professional Service

Font styles to use
Serif

Requirements
Must have
• - Professional, Modern TRI-FOLD Brochure Design for United States Based Company
• - Please show diverse group of professionals pictures similar to the ones on our website. One pic must include an African American female and one pic must include an African male. Or both an African American female and male can be include in the group of other races. But All the group photos must be diverse in race and include both male and female.
• - Please show pics of one business professional too
• a diverse group photo would be nice on the front cover...so we can show diversity and inclusion from the start
Should not have
• - Please DO NOT use the same pictures on our website.

```html
<!DOCTYPE html>
<html lang="en">
<head>
<meta charset="utf-8">
<title>Pelvor Staffing Partners – Brochure</title>
<link href="https://fonts.googleapis.com/css2?family=Source+Serif+4:opsz,wght@8..60,300;8..60,400;8..60,600&display=swap" rel="stylesheet">
<style>
  :root {
    --red: #b3080e;
    --red-dark: #8a0a10;
    --red-text: #a30d12;
    --black: #111;
    --ink: #2a2a2a;
    --paper: #ffffff;
    --fold: rgba(0,0,0,0.06);
  }
  html, body { margin: 0; padding: 0; overflow: hidden; }
  body { width: 1200px; height: 887px; background: var(--paper); font-family: "Source Serif 4", Georgia, serif; }
  .brochure { position: relative; width: 1200px; height: 887px; overflow: hidden; background: linear-gradient(90deg, #fff 0 400px, #f4f4f4 400px 800px, #f7f7f7 800px); }
  .photo { position: absolute; }
  .photo-professional { left: 0; top: 378px; width: 400px; height: 360px; background: linear-gradient(160deg, #e9eef2 0%, #f7f8f9 45%, #d9dde2 100%); }
  .photo-team { left: 500px; top: 318px; width: 700px; height: 480px; background: radial-gradient(ellipse at 55% 55%, #dfe6e6 0%, #c9cfd2 45%, #9aa1a6 100%);
    -webkit-mask-image: linear-gradient(180deg, transparent 0, #000 70px); mask-image: linear-gradient(180deg, transparent 0, #000 70px); }
  .waves { position: absolute; inset: 0; }
  .fold { position: absolute; top: 0; bottom: 0; width: 1px; background: var(--fold); }
  .section-tab { position: absolute; top: 24px; height: 37px; display: flex; align-items: center; }
  .section-tab .label { background: var(--red); color: #fff; height: 100%; display: flex; align-items: center; font-size: 19px; font-weight: 400; padding-left: 38px; box-sizing: border-box; white-space: nowrap; clip-path: polygon(0 0, 100% 0, calc(100% - 20px) 100%, 0 100%); }
  .section-tab .slash { width: 22px; height: 100%; background: var(--black); margin-left: -6px; clip-path: polygon(0 0, 45% 0, 100% 100%, 55% 100%); }
  .tab-who { left: 0; } .tab-who .label { width: 238px; }
  .tab-diff { left: 400px; } .tab-diff .label { width: 362px; }
  .who { position: absolute; left: 38px; top: 84px; width: 320px; }
  .subhead { margin: 0 0 8px; color: var(--red-text); font-size: 16px; font-weight: 600; line-height: 22px; white-space: nowrap; }
  .who p { margin: 0; font-size: 13px; line-height: 18.2px; color: var(--ink); text-align: justify; }
  .difference { position: absolute; left: 438px; top: 84px; width: 340px; }
  .checklist { list-style: none; margin: 0; padding: 0; }
  .checklist li { position: relative; padding-left: 24px; font-size: 13.5px; line-height: 18px; color: var(--ink); margin-bottom: 13px; }
  .checklist svg { position: absolute; left: 0; top: 2px; }
  .headline { position: absolute; left: 855px; top: 36px; margin: 0; color: var(--red-text); font-size: 38px; font-weight: 300; line-height: 50px; }
  .contact { position: absolute; width: 400px; text-align: center; color: #fff; }
  .contact .phone { font-size: 24px; font-weight: 300; display: flex; justify-content: center; align-items: center; gap: 10px; }
  .contact .web { margin-top: 6px; font-size: 16px; font-weight: 300; display: flex; justify-content: center; align-items: center; gap: 8px; }
  .contact-left { left: 0; top: 810px; }
  .contact-right { left: 825px; top: 810px; }
</style>
</head>
<body>
<main class="brochure">
  <div class="photo photo-professional" role="img" aria-label="Smiling business professional seated at a desk in a bright office"></div>
  <div class="photo photo-team" role="img" aria-label="Overhead view of a diverse team meeting around a glass conference table"></div>

  <svg class="waves" width="1200" height="887" viewBox="0 0 1200 887" aria-hidden="true">
    <path d="M0,575 C320,770 820,880 1200,655 L1200,887 L0,887 Z" fill="#111"/>
    <path d="M0,606 C320,790 820,895 1200,680 L1200,887 L0,887 Z" fill="var(--red-dark)"/>
    <path d="M0,690 C320,830 820,905 1200,706 L1200,887 L0,887 Z" fill="#fff"/>
    <path d="M0,722 C320,852 820,925 1200,730 L1200,887 L0,887 Z" fill="var(--red)"/>
  </svg>

  <div class="fold" style="left:400px"></div>
  <div class="fold" style="left:800px"></div>

  <div class="section-tab tab-who"><span class="label">Who We Are</span><span class="slash"></span></div>
  <section class="who">
    <h2 class="subhead">A Top-Notch Resource for Administrative,<br>Human Resources, and Accounting Talent</h2>
    <p>Pelvor Staffing Partners is a professional search firm that specializes in providing top-notch administrative, human resources, and accounting talent. We provide best-in-class talent to companies seeking to simplify their recruiting process, increase efficiency, and optimize productivity. Each search is customized based on our client's unique requirements. We provide quality, timely, and efficient services. Our recruiters are highly skilled in identifying, screening, interviewing, and assessing candidates across various industries. We develop a partnership with our client and candidate in order to make the recruitment process a success for both parties.</p>
  </section>

  <div class="section-tab tab-diff"><span class="label">Experience the Pelvor Difference</span><span class="slash"></span></div>
  <section class="difference">
    <h2 class="subhead">We use our proprietary P-Strategy<br>approach to deliver high-quality results.</h2>
    <ul class="checklist">
      <li><svg width="14" height="13" viewBox="0 0 14 13"><path d="M1,7 L5,11 L13,1" fill="none" stroke="var(--red)" stroke-width="2.4"/></svg>Top-Notch Talent. We will only present candidates who meet 90% of your job requirements.</li>
      <li><svg width="14" height="13" viewBox="0 0 14 13"><path d="M1,7 L5,11 L13,1" fill="none" stroke="var(--red)" stroke-width="2.4"/></svg>Thorough. We listen to your needs and develop a recruiting checklist to make sure we cover all basis.</li>
      <li><svg width="14" height="13" viewBox="0 0 14 13"><path d="M1,7 L5,11 L13,1" fill="none" stroke="var(--red)" stroke-width="2.4"/></svg>Tenacious. We are passionate and persistent about meeting your expectations.</li>
      <li><svg width="14" height="13" viewBox="0 0 14 13"><path d="M1,7 L5,11 L13,1" fill="none" stroke="var(--red)" stroke-width="2.4"/></svg>Timely. We deliver quality results on time.</li>
    </ul>
  </section>

  <h1 class="headline">We can find<br>the right talent for<br>your hiring needs.</h1>

  <div class="contact contact-left">
    <div class="phone"><svg width="20" height="20" viewBox="0 0 20 20"><circle cx="10" cy="10" r="8.5" fill="none" stroke="#fff" stroke-width="1.5"/><path d="M7,5.5 L8.6,7.6 L7.8,8.8 C8.5,10.3 9.7,11.5 11.2,12.2 L12.4,11.4 L14.5,13 L13.4,14.6 C10,14.4 5.6,10 5.4,6.6 Z" fill="#fff"/></svg>555-014-0627</div>
    <div class="web"><svg width="13" height="13" viewBox="0 0 14 14"><circle cx="7" cy="7" r="6" fill="none" stroke="#fff" stroke-width="1.2"/><ellipse cx="7" cy="7" rx="2.6" ry="6" fill="none" stroke="#fff" stroke-width="1"/><path d="M1,7 H13 M2,4 H12 M2,10 H12" stroke="#fff" stroke-width="1"/></svg>www.pelvorstaffingpartners.example</div>
  </div>
  <div class="contact contact-right">
    <div class="phone"><svg width="20" height="20" viewBox="0 0 20 20"><circle cx="10" cy="10" r="8.5" fill="none" stroke="#fff" stroke-width="1.5"/><path d="M7,5.5 L8.6,7.6 L7.8,8.8 C8.5,10.3 9.7,11.5 11.2,12.2 L12.4,11.4 L14.5,13 L13.4,14.6 C10,14.4 5.6,10 5.4,6.6 Z" fill="#fff"/></svg>555-014-0627</div>
    <div class="web"><svg width="13" height="13" viewBox="0 0 14 14"><circle cx="7" cy="7" r="6" fill="none" stroke="#fff" stroke-width="1.2"/><ellipse cx="7" cy="7" rx="2.6" ry="6" fill="none" stroke="#fff" stroke-width="1"/><path d="M1,7 H13 M2,4 H12 M2,10 H12" stroke="#fff" stroke-width="1"/></svg>www.pelvorstaffingpartners.example</div>
  </div>
</main>
</body>
</html>
```